Crazy, Different WOMENS PREWORKOUT Packaging Label

We need a MODERN, CRAZY, FUN packaging preworkout label for WOMEN.
There are no limits for this project, be wild and crazy and DIFFERENT.

The name of the product is VELTANE BLUSH and it is a gym preworkout supplement for women.
The company is called KORVAPLENTIX.

We're looking to convey strength, femininity, uniqueness, health, vitality, vigor, focus, concentration, energy, stamina.

and above all HEALTH
Updates

Project Deadline Extended Reason: Hello All, thanks for your submissions so far. In the interest of receiving the best designs, we will extend the deadline by 5 days. We appreciate your effort and look forward to further revisions to hone and perfect the concepts already submitted. Thank you all for your effort so far! Added Saturday, January 7, 2017

Target Market(s)

Sports Women and Women Gym goers

Font styles to use
Serif
Sans Serif
Decorative
Other font styles liked:
• AR Destine

Requirements
Must have
• It must have SOME red in it somewhere because the product is called VELTANE BLUSH but it does NOT have to be the dominating color.
• It must include our Company logo on the label too, but the company logo and the product name should be harmonious. It should be obvious which part of the design is the company logo and which part is the name of the product.
• Include any one of the Company Logo Strips on the label (see reference files) can make it any color!
Nice to have
• Nice to have something unique and different but appealing to women. but NOT stereotypical of women...
• It should be something strong, elite and feminine BUT NOT bubblegum pink and rainbows...
• The jar is a round white jar.
• Try make it look clean, healthful, effective.
• I'm open to crazy and simple designs.
Should not have
• Should not JUST be pink and purple and stereotypical to women.
• It CAN have pink and purple in it though.

```html
<!DOCTYPE html>
<html lang="en">
<head>
<meta charset="utf-8">
<title>Veltane Blush – Pre-workout Label</title>
<link rel="stylesheet" href="https://fonts.googleapis.com/css2?family=Comfortaa:wght@300;400&family=Oswald:wght@400;500;600&family=Source+Sans+3:wght@400;600&display=swap">
<style>
  :root {
    --blush-red: #ec1c24;
    --deep-red: #c4121a;
    --ink: #1c1c1c;
    --label-white: #fbfbfb;
    --soft-grey: #9a9a9a;
    --line-grey: #b8b8b8;
    --backdrop: #ececec;
  }
  * { box-sizing: border-box; margin: 0; padding: 0; }
  html, body { width: 1200px; height: 1200px; overflow: hidden; }
  body {
    background: var(--backdrop);
    font-family: "Source Sans 3", sans-serif;
    color: var(--ink);
    position: relative;
  }
  .label {
    position: absolute;
    left: 20px; top: 270px;
    width: 1160px; height: 660px;
    background: var(--label-white);
    border-radius: 6px;
    box-shadow: 0 4px 18px rgba(0,0,0,.12);
    overflow: hidden;
  }
  /* ---------- ingredients panel ---------- */
  .ingredients {
    position: absolute;
    left: 30px; top: 80px;
    width: 210px; height: 500px;
    border: 2px solid var(--line-grey);
    border-radius: 22px;
    padding: 22px 18px;
  }
  .ingredients h3 {
    font-family: "Oswald", sans-serif;
    font-weight: 500;
    font-size: 15px;
    letter-spacing: .5px;
    text-align: right;
    margin-bottom: 12px;
  }
  .ingredients p {
    font-family: "Oswald", sans-serif;
    font-size: 13px;
    line-height: 1.45;
  }
  /* ---------- back panel ---------- */
  .back-panel {
    position: absolute;
    left: 270px; top: 0;
    width: 390px; height: 100%;
  }
  .back-claim {
    position: absolute;
    left: 0; top: 150px;
    width: 370px; height: 150px;
    background: var(--ink);
    color: #fff;
    border-radius: 0 16px 16px 0;
    padding: 26px 22px;
    font-size: 20px;
    line-height: 1.35;
  }
  .contact {
    position: absolute;
    left: 0; top: 350px;
    width: 370px;
    text-align: center;
    font-family: "Oswald", sans-serif;
    font-weight: 500;
    font-size: 18px;
    line-height: 2.2;
  }
  /* ---------- front panel ---------- */
  .front-panel {
    position: absolute;
    left: 660px; top: 0;
    width: 500px; height: 100%;
  }
  .name-band {
    position: absolute;
    left: 10px; top: 70px;
    width: 480px; height: 110px;
    background: var(--blush-red);
    border: 3px solid var(--deep-red);
    border-radius: 12px;
    color: #fff;
    font-family: "Comfortaa", sans-serif;
    font-weight: 300;
    font-size: 58px;
    letter-spacing: -1px;
    line-height: 104px;
    text-align: center;
    z-index: 2;
  }
  .accent-ring {
    position: absolute;
    left: 40px; top: 165px;
    width: 90px; height: 90px;
    border: 3px solid var(--blush-red);
    border-radius: 50%;
    background: var(--label-white);
    z-index: 3;
  }
  .tagline-band {
    position: absolute;
    left: 160px; top: 180px;
    width: 340px; height: 160px;
    background: var(--ink);
    border-radius: 14px 0 0 14px;
    color: #fff;
    font-family: "Oswald", sans-serif;
    font-size: 24px;
    line-height: 1.3;
    text-align: center;
    padding-top: 18px;
  }
  .facts {
    position: absolute;
    left: 20px; top: 360px;
    display: grid;
    grid-template-columns: repeat(3, 82px);
    gap: 10px;
  }
  .fact {
    width: 82px; height: 82px;
    border-radius: 50%;
    border: 3px solid var(--blush-red);
    box-shadow: inset 0 0 0 3px var(--label-white), inset 0 0 0 5px var(--line-grey);
    display: flex; flex-direction: column;
    align-items: center; justify-content: center;
    font-family: "Oswald", sans-serif;
    line-height: 1;
  }
  .fact .value { font-size: 30px; color: var(--deep-red); }
  .fact .value small { font-size: 16px; }
  .fact .unit { font-size: 13px; font-weight: 600; text-transform: uppercase; margin-top: 3px; }
  .fact.is-muted .value { color: var(--soft-grey); }
  .fact.is-muted { border-color: var(--deep-red); }
  .company-box {
    position: absolute;
    left: 320px; top: 450px;
    width: 160px; height: 96px;
    border: 2px solid var(--line-grey);
    border-radius: 12px;
    display: flex; flex-direction: column;
    align-items: center; justify-content: center;
    gap: 8px;
  }
  .company-box .mark {
    width: 28px; height: 28px;
    background: var(--blush-red);
  }
  .company-box .name {
    font-family: "Oswald", sans-serif;
    font-weight: 600;
    font-size: 17px;
    color: var(--ink);
  }
  .net-weight {
    position: absolute;
    left: 300px; top: 570px;
    width: 180px; height: 46px;
    border: 2px solid var(--line-grey);
    border-radius: 10px;
    font-family: "Oswald", sans-serif;
    font-weight: 500;
    font-size: 20px;
    line-height: 42px;
    text-align: center;
  }
</style>
</head>
<body>
  <section class="label">
    <aside class="ingredients">
      <h3>INGREDIENTS</h3>
      <p>Beet root powder, L-citrulline, beta-alanine, green tea extract, natural caffeine, taurine, vitamin B6, vitamin B12, magnesium citrate, natural cherry flavor, citric acid, stevia leaf extract, sea salt.</p>
    </aside>

    <div class="back-panel">
      <p class="back-claim">Each 8 fluid oz. serving of Veltane Blush delivers a scientifically balanced and targeted array of nutrients to help you get the most out of your workouts</p>
      <div class="contact">
        <div>KORVAPLENTIX</div>
        <div>www.korvaplentix</div>
        <div>1 800 555-0142</div>
        <div>frendlo.com/veltaneblush</div>
      </div>
    </div>

    <div class="front-panel">
      <h1 class="name-band">veltane blush</h1>
      <div class="accent-ring" aria-hidden="true"></div>
      <div class="tagline-band">Dietary Pre-workout<br>Supplement<br>for<br>ACTIVE WOMEN</div>

      <div class="facts">
        <div class="fact"><span class="value">450</span><span class="unit">Calories</span></div>
        <div class="fact"><span class="value">23<small>g</small></span><span class="unit">Protein</span></div>
        <div class="fact is-muted"><span class="value">23<small>g</small></span><span class="unit">Protein</span></div>
        <div class="fact"><span class="value">5<small>g</small></span><span class="unit">Sat Fat</span></div>
        <div class="fact"><span class="value">4<small>g</small></span><span class="unit">Fiber</span></div>
        <div class="fact is-muted"><span class="value">4<small>g</small></span><span class="unit">Fiber</span></div>
        <div class="fact"><span class="value">13<small>g</small></span><span class="unit">Sugars</span></div>
        <div class="fact"><span class="value">23<small>g</small></span><span class="unit">Protein</span></div>
        <div class="fact is-muted"><span class="value">23<small>g</small></span><span class="unit">Protein</span></div>
      </div>

      <div class="company-box">
        <span class="mark"></span>
        <span class="name">KORVAPLENTIX</span>
      </div>
      <div class="net-weight">168.3 g (8.18 oz)</div>
    </div>
  </section>
</body>
</html>
```